依頼詳細
A4サイズカラー両面チラシのデザイン
・光触媒コーティングサービスのメリットが伝わるもの
・イラストを使用して、わかりやすいもの
※チラシデザインを決定させていただき、それをベースにLPデザインも追加依頼予定(別途料金)
記載項目
株式会社Sorano Works
山口県山口市小郡若葉町3-17
TEL 083-512-4937
サイズ
A4
ページ数
両面
希望イメージ
シンプル 複雑
単色 カラフル
暗い 明るい
日常 高級
遊び心 厳粛
未来的 伝統的
女性的 男性的
希望する色
黄・オレンジ系、緑系、青系
納品ファイル
• イラストレーター形式 (.ai)
■ 選んだ理由

完成イメージに近かったです。

■ 提案者全員のお礼・コメント

皆様、ご提案ありがとうございました。

```html
<!DOCTYPE html>
<html lang="ja">
<head>
<meta charset="utf-8">
<title>光触媒コーティング チラシ</title>
<link href="https://fonts.googleapis.com/css2?family=Noto+Sans+JP:wght@400;700;900&family=Noto+Serif+JP:wght@700;900&display=swap" rel="stylesheet">
<style>
  :root{
    --navy:#1d3c8c;
    --blue:#2f7fd0;
    --sky:#dcefff;
    --sky-deep:#b9dcf7;
    --red:#e0242b;
    --yellow:#fde04a;
    --gray:#9c9c9c;
    --ink:#222;
    --white:#fff;
  }
  *{margin:0;padding:0;box-sizing:border-box}
  html,body{width:846px;height:1200px;overflow:hidden;background:#fff}
  body{font-family:"Noto Sans JP",sans-serif;color:var(--ink)}
  .flyer{position:relative;width:846px;height:1200px;overflow:hidden;
    background:linear-gradient(180deg,var(--sky) 0%,var(--sky-deep) 100%)}
  .abs{position:absolute}
  .hero-photo{left:0;top:0;width:846px;height:410px;
    background:linear-gradient(135deg,#f4efe6 0%,#e8dccb 55%,#cdb79a 100%)}
  .worker-illust{left:0;top:0;width:95px;height:110px;
    background:linear-gradient(180deg,#c9d6b4,#7f9a63)}
  .header-copy{left:105px;top:8px;width:600px}
  .header-copy .lead{font-size:24px;font-weight:700;display:flex;align-items:center;gap:10px}
  .header-copy .free{background:var(--red);color:var(--white);padding:2px 10px;font-weight:900}
  .header-copy .trust{font-size:20px;font-weight:700;margin-top:8px}
  .price-row{display:flex;align-items:center;gap:10px;margin-top:6px}
  .price-row .note{font-size:11px;line-height:1.3}
  .price-row .cheap{color:var(--red);font-size:14px;font-weight:700}
  .price-row .room{background:#111;color:var(--white);font-weight:900;font-size:18px;padding:2px 8px}
  .price-row .price{color:var(--red);font-weight:900;font-size:30px}
  .price-row .price small{font-size:16px}
  .brand{right:0;top:0;width:128px;height:80px;background:var(--white);
    display:flex;align-items:center;justify-content:center;gap:6px;font-size:15px;font-weight:700;color:var(--navy)}
  .brand .mark{width:12px;height:12px;background:var(--navy)}
  .headline{left:0;width:846px;top:412px;text-align:center;font-family:"Noto Serif JP",serif;
    font-weight:900;font-size:54px;color:var(--navy);letter-spacing:2px}
  .product-name{left:110px;top:500px;width:540px;height:58px;background:var(--gray);
    color:var(--white);font-size:36px;font-weight:700;padding-left:40px;line-height:58px;letter-spacing:6px}
  .intro{left:110px;top:568px;font-size:17px;font-weight:700}
  .benefits{left:110px;top:600px;display:flex;align-items:center;gap:12px}
  .benefit{border:3px solid var(--red);background:var(--white);color:var(--red);font-weight:900;
    font-size:22px;padding:0 16px;height:50px;display:flex;align-items:center;justify-content:center;text-align:center;line-height:1.15}
  .plus{font-size:30px;font-weight:900;color:var(--red)}
  .footnote{left:110px;top:662px;font-size:12px}
  .badge{left:672px;top:540px;width:160px;height:130px;border-radius:50%;background:var(--white);
    border:3px solid var(--red);display:flex;flex-direction:column;align-items:center;justify-content:center;line-height:1.1}
  .badge .target{font-size:12px;font-weight:700;color:var(--navy);text-align:center}
  .badge .rate{font-size:38px;font-weight:900;color:var(--red)}
  .badge .rate small{font-size:20px}
  .badge .down{font-size:22px;font-weight:900;color:var(--red)}
  .tech-line{left:110px;top:712px;font-size:30px;font-weight:900;color:var(--navy)}
  .coating-band{left:110px;top:758px;width:720px;height:58px;background:var(--blue);
    color:var(--white);font-size:44px;font-weight:900;line-height:58px;padding-left:24px;letter-spacing:2px}
  .effect-panel{left:110px;top:816px;width:720px;height:150px;background:var(--yellow)}
  .effect-title{left:128px;top:826px;width:500px;font-size:92px;font-weight:900;color:var(--red);line-height:1.4;letter-spacing:2px;white-space:nowrap}
  .woman-illust{left:640px;top:772px;width:190px;height:194px;
    background:linear-gradient(160deg,#f6d38a 0%,#e9a35c 100%);border-radius:12px}
  .effects{left:110px;top:985px;display:flex;gap:12px}
  .effect{width:134px;height:62px;border:3px solid var(--red);background:var(--white);color:var(--red);
    font-size:32px;font-weight:900;display:flex;align-items:center;justify-content:center}
  .effect.primary{background:var(--red);color:var(--white)}
  .effect-note{left:110px;top:1064px;width:720px;font-size:15px;font-weight:700;color:var(--ink)}
  .company{left:110px;top:1110px;width:720px;font-size:16px;font-weight:700;color:var(--navy);display:flex;gap:24px}
</style>
</head>
<body>
<div class="flyer">
  <div class="abs hero-photo" role="img" aria-label="笑顔の子どもと母親が床に座るリビングの写真。壁にウイルスのバツ印イラスト"></div>
  <div class="abs worker-illust" role="img" aria-label="作業服姿のスタッフのイラスト"></div>

  <div class="abs header-copy">
    <p class="lead">まずは、お気軽に <span class="free">無料お見積もりを!</span></p>
    <p class="trust">◆◆◆◆◆お任せください!</p>
    <div class="price-row">
      <p class="note">現地調査の上で<br><span class="cheap">低価格を実現</span></p>
      <span class="room">6帖間</span>
      <span class="price">39,000<small>円〜</small></span>
    </div>
  </div>

  <div class="abs brand"><span class="mark"></span>Sorano Works</div>

  <h1 class="abs headline">壁・床・天井、安心</h1>

  <div class="abs product-name">商品名</div>
  <p class="abs intro">家庭のアルコール消毒等も必要がなく、一度の施術で</p>
  <div class="abs benefits">
    <div class="benefit" style="width:210px">長期間抗菌</div>
    <span class="plus">+</span>
    <div class="benefit" style="width:260px;font-size:19px">ウイルスを<br>分解・不活性化</div>
  </div>
  <p class="abs footnote">※酸化チタン光触媒の効果は長期間持続します(使用環境により異なります)</p>

  <div class="abs badge">
    <span class="target">A型インフルエンザ<br>ウイルス</span>
    <span class="rate">99.9<small>%</small></span>
    <span class="down">減少</span>
  </div>

  <p class="abs tech-line">進化した光触媒超微粒子酸化チタンで</p>
  <div class="abs effect-panel"></div>
  <div class="abs coating-band">光触媒コーティング</div>
  <p class="abs effect-title">脱臭・除菌</p>
  <div class="abs woman-illust" role="img" aria-label="ウイルスを退治する女性のイラスト"></div>

  <div class="abs effects">
    <div class="effect primary">防カビ</div>
    <div class="effect">抗菌</div>
    <div class="effect">除菌</div>
    <div class="effect">防臭</div>
    <div class="effect">防汚</div>
  </div>
  <p class="abs effect-note">インフルエンザウイルス、ノロウイルス、O-157、黄色ブドウ球菌などの除菌・抗菌が可能です</p>
  <div class="abs company">
    <span>株式会社Sorano Works</span>
    <span>山口県山口市小郡若葉町3-17</span>
    <span>TEL 083-512-4937</span>
  </div>
</div>
</body>
</html>
```